Business Card for Nail Art business
Gloss Haven (Card to be non-standard sized)
Business Card for Nail Art business -
Creative Brief
Bright & Fun-filled
Marisa Quell
Ms.
Brimwood Vale and Ashcombe
marisaqv@postlark.net
The business card is to be NON-standard sized, double sided I would wish it to be either 90x45mm or 80x45mm, however it is up to you to find a size that fits your design best, but it must be smaller than standard Please incorporate the logo Feel free to use any font that fits you Please tell me the dimensions of your design/s
The back should have the logo as the main focus, whereas the front should just hold the general contact details, etc. Be creative and see where it goes as even myself is unsure of what I exactly want Feel free to PM me if any questions

```html
<!DOCTYPE html>
<html lang="en">
<head>
<meta charset="utf-8">
<title>Gloss Haven – Business Card</title>
<link rel="stylesheet" href="https://fonts.googleapis.com/css2?family=Noto+Serif:wght@400;700&family=Open+Sans:wght@700&display=swap">
<style>
  :root {
    --page-bg: #ecebe8;
    --card-white: #ffffff;
    --brand-red: #d0142c;
    --brand-red-dark: #9c0c1e;
    --swoosh-black: #111111;
    --swoosh-grey: #c9c9c9;
    --text-light: #ffffff;
    --logo-red: #c8102e;
  }
  html, body {
    margin: 0;
    width: 1200px;
    height: 646px;
    overflow: hidden;
    background: var(--page-bg);
  }
  .card {
    position: absolute;
    left: 100px;
    top: 73px;
    width: 1000px;
    height: 500px;
    background: var(--card-white);
    box-shadow: 0 6px 18px rgba(0,0,0,0.18);
    overflow: hidden;
  }
  .card-shapes {
    position: absolute;
    inset: 0;
  }
  .holder-name {
    position: absolute;
    left: 44px;
    top: 48px;
    margin: 0;
    font-family: "Open Sans", Arial, sans-serif;
    font-weight: 700;
    font-size: 26px;
    color: var(--text-light);
  }
  .contact-list {
    position: absolute;
    left: 44px;
    top: 290px;
    margin: 0;
    padding: 0;
    list-style: none;
    font-family: "Noto Serif", Georgia, serif;
    font-size: 21px;
    color: var(--text-light);
  }
  .contact-list li {
    display: flex;
    align-items: center;
    gap: 12px;
    margin-bottom: 14px;
  }
  .contact-list .location { margin-bottom: 22px; }
  .contact-icon { width: 20px; height: 20px; flex: none; }
  .brand-mark {
    position: absolute;
    left: 580px;
    top: 212px;
    display: flex;
    align-items: center;
    gap: 14px;
  }
  .brand-dot {
    width: 58px;
    height: 58px;
    border-radius: 50%;
    background: var(--logo-red);
  }
  .brand-name {
    font-family: "Noto Serif", Georgia, serif;
    font-weight: 700;
    font-size: 48px;
    letter-spacing: 1px;
    color: var(--logo-red);
    text-transform: uppercase;
  }
</style>
</head>
<body>
  <section class="card" aria-label="Gloss Haven business card">
    <svg class="card-shapes" viewBox="0 0 1000 500" width="1000" height="500" aria-hidden="true">
      <defs>
        <linearGradient id="redPanel" x1="0" y1="0" x2="1" y2="1">
          <stop offset="0" stop-color="var(--brand-red)"/>
          <stop offset="1" stop-color="var(--brand-red-dark)"/>
        </linearGradient>
      </defs>
      <path class="swoosh-shadow" d="M448,0 C500,160 520,360 600,500 H585 C510,360 490,160 440,0 Z" fill="var(--swoosh-grey)"/>
      <path class="swoosh-line" d="M432,0 C482,160 500,350 580,500 H560 C488,350 470,160 424,0 Z" fill="var(--swoosh-black)"/>
      <path class="red-panel" d="M0,0 H430 C476,160 492,350 566,500 H0 Z" fill="url(#redPanel)"/>
    </svg>

    <h1 class="holder-name">Ms.Marisa Quell</h1>

    <ul class="contact-list">
      <li class="location">Brimwood Vale &amp; Ashcombe</li>
      <li class="phone">
        <svg class="contact-icon" viewBox="0 0 24 24" aria-hidden="true">
          <path d="M6.6 10.8a15 15 0 0 0 6.6 6.6l2.2-2.2a1 1 0 0 1 1-.25 11.4 11.4 0 0 0 3.6.57 1 1 0 0 1 1 1V20a1 1 0 0 1-1 1A17 17 0 0 1 3 4a1 1 0 0 1 1-1h3.5a1 1 0 0 1 1 1c0 1.25.2 2.45.57 3.57a1 1 0 0 1-.25 1z" fill="#fff"/>
        </svg>
        0490317265
      </li>
      <li class="email">
        <svg class="contact-icon" viewBox="0 0 24 24" aria-hidden="true">
          <rect x="2" y="5" width="20" height="14" rx="2" fill="#fff"/>
          <path d="M3 6.5l9 6.5 9-6.5" fill="none" stroke="#b00f24" stroke-width="1.6"/>
        </svg>
        marisaqv@postlark.net
      </li>
    </ul>

    <div class="brand-mark">
      <span class="brand-dot" aria-hidden="true"></span>
      <span class="brand-name">Gloss Haven</span>
    </div>
  </section>
</body>
</html>
```